Signage for Brightwell Academy - Exterior

Size 32 ft x 5 ft 11 inches. It will be installed at a height of 25 feet. Should contain the Logo, Address, some courses to give an idea about what we do. The signage is installed on the 2nd floor, so the minimum size of letters would be as in the old signage design attached. The font size of the bottom line of our existing signage is as small as we should go. Basically it should be such that the first glance gives us an idea that it is a Brightwell Academy. You are allowed to change the logo colors, but the font and design will remain the same.
Updates

Reason: some extra time might be needed to improve the designs and get new inputs. need some out of the box designing.

Target Market(s)

High School and College going teens who wish to learn software skills for graphics and animation

Industry/Entity Type

Education

Font styles to use
Other font styles liked:
• Utopia

Colors

Designer to choose colors to be used in the design.

Requirements
Must have
• Logo, Address, Phone Number, website address, what we do.
• 1. Please refer to the image of our old signage uploaded. The font size of the courses mentioned at the bottom of the signage "ANIMATION, GAMING.." is the smallest size which is legible from the ground level.
• 2. We would like at least the web address in legible font size and if possible the phone number too. The physical address could be a little smaller as in the old signage, as that is not a calling factor and in case someone is interested, they can walk closer and read the address.
• 3. The calling factors would be a few courses and some graphics depicting what we do in the first look.
• 4.You are allowed to change the logo colors, but the font and design will remain the same. Prefer usage of Ubuntu font for text.
• 5. Prefer minimalist look and not cluttered. I feel mentioning more courses is making the signage cluttered. we can limit it to 3 courses.
Nice to have
• Graphics to suggest what we do. It should be eye catching. The graphic should be such that speaks of what we do. It should be suggestive.
Should not have
• It should not be too busy

```html
<!DOCTYPE html>
<html lang="en">
<head>
<meta charset="utf-8">
<title>Brightwell Academy – Exterior Signage</title>
<link rel="stylesheet" href="https://fonts.googleapis.com/css2?family=Ubuntu:wght@400;500;700&display=swap">
<style>
  :root {
    --backdrop: #e9ecf0;
    --navy: #0b2a61;
    --teal: #2bb3bd;
    --orange: #f5a00f;
    --white: #ffffff;
  }
  * { margin: 0; padding: 0; box-sizing: border-box; }
  html, body {
    width: 1200px;
    height: 480px;
    overflow: hidden;
    background: var(--backdrop);
    font-family: "Ubuntu", sans-serif;
  }
  .signboard {
    position: absolute;
    left: 20px;
    top: 149px;
    width: 1160px;
    height: 182px;
    background: var(--navy);
    overflow: hidden;
    box-shadow: 0 3px 10px rgba(0, 0, 0, 0.25);
  }
  .signboard-panels {
    position: absolute;
    inset: 0;
  }
  .brand-name {
    position: absolute;
    left: 56px;
    top: 72px;
    font-size: 42px;
    font-weight: 500;
    letter-spacing: 1px;
    color: var(--white);
    line-height: 1;
    white-space: nowrap;
  }
  .tagline {
    position: absolute;
    left: 355px;
    top: 30px;
    font-size: 44px;
    font-weight: 700;
    color: var(--orange);
    line-height: 1;
    letter-spacing: 0.5px;
    white-space: nowrap;
  }
  .web-address {
    position: absolute;
    right: 385px;
    top: 120px;
    font-size: 34px;
    font-weight: 400;
    color: var(--white);
    line-height: 1;
    white-space: nowrap;
  }
  .web-address .domain {
    color: var(--orange);
    font-weight: 700;
  }
  .course-list {
    position: absolute;
    left: 862px;
    top: 28px;
    list-style: none;
  }
  .course-list li {
    display: flex;
    align-items: center;
    height: 44.5px;
    font-size: 39px;
    font-weight: 700;
    color: var(--white);
    line-height: 1;
  }
  .course-list li::before {
    content: "";
    width: 19px;
    height: 19px;
    margin-right: 20px;
    background: linear-gradient(to right, rgba(255, 255, 255, 0), rgba(255, 255, 255, 0.95));
  }
</style>
</head>
<body>
  <div class="signboard">
    <svg class="signboard-panels" width="1160" height="182" viewBox="0 0 1160 182" aria-hidden="true">
      <polygon points="838,0 855,0 797,182 780,182" fill="var(--white)"/>
      <polygon points="855,0 1160,0 1160,182 797,182" fill="var(--teal)"/>
    </svg>

    <div class="brand-name">BRIGHTWELL</div>
    <div class="tagline">DIGITAL ACADEMY</div>
    <div class="web-address">www.<span class="domain">brightwell</span>.in</div>

    <ul class="course-list">
      <li>VFX</li>
      <li>ANIMATION</li>
      <li>GAMING</li>
    </ul>
  </div>
</body>
</html>
```